Deactivated Coal-Fired Power Plant to be redeveloped into a Green Energy Campus.

Want a striking business card statement that introduces our concept project to provide economic and community recovery to a former rural coal community in western PA.
Essentially 12 project representatives that will lead both the demolition of an existing power plant and the redevelopment to a new Green energy site.
Business Card should reflect our effort.
We are open to ideas.

Target Market(s)

Energy and Power Generation industries

Industry/Entity Type

Power Generation and Data Centers

Contact Information for Business Card

Included in uploaded materials

Font styles to use
Sans Serif
Other font styles liked:
• Arial, Calibri

Requirements
Must have
• Multiple colors

```html
<!DOCTYPE html>
<html lang="en">
<head>
<meta charset="utf-8">
<title>Ridgeline Renewal – Business Card</title>
<link href="https://fonts.googleapis.com/css2?family=Lato:wght@700;900&family=Oswald:wght@300;400;500&display=swap" rel="stylesheet">
<style>
  :root {
    --bg: #d6d6d6;
    --card: #ffffff;
    --ink: #111111;
    --green: #109a49;
    --rule: #c9c9c9;
  }
  * { margin: 0; padding: 0; box-sizing: border-box; }
  html, body {
    width: 1200px; height: 900px; overflow: hidden;
    background: var(--bg);
  }
  .sheet {
    width: 1200px; height: 900px;
    display: flex; flex-direction: column; align-items: center; justify-content: center;
    gap: 40px;
  }
  .card {
    position: relative;
    width: 700px; height: 400px;
    background: var(--card);
    box-shadow: 0 6px 18px rgba(0,0,0,0.18);
    overflow: hidden;
  }
  .card__band {
    position: absolute; left: 0; bottom: 0;
    width: 700px; height: 60px;
  }
  .brand {
    display: flex; align-items: center; gap: 16px;
  }
  .brand__dot {
    width: 74px; height: 74px; border-radius: 50%;
    background: var(--green);
    flex: none;
  }
  .brand__name {
    font-family: 'Lato', Arial, sans-serif;
    font-weight: 900;
    font-size: 34px;
    line-height: 1;
    color: var(--ink);
    text-transform: uppercase;
    letter-spacing: 0.5px;
    white-space: nowrap;
  }
  .brand__line { display: block; }
  .card--front .brand {
    position: absolute; left: 50%; top: 160px;
    transform: translate(-50%, -50%);
  }
  .card--back .brand {
    position: absolute; left: 0; top: 210px;
    width: 340px;
    justify-content: center;
    transform: translateY(-50%);
  }
  .card--back .brand__name { font-size: 27px; }
  .card--back .brand__dot { width: 62px; height: 62px; }
  .divider {
    position: absolute; left: 340px; top: 40px;
    width: 1px; height: 270px;
    background: var(--rule);
  }
  .contact {
    position: absolute; left: 380px; top: 58px;
    font-family: 'Oswald', Arial, sans-serif;
    color: var(--ink);
  }
  .contact__name { font-weight: 500; font-size: 30px; line-height: 1.15; }
  .contact__title { font-weight: 400; font-size: 19px; color: var(--green); margin-bottom: 26px; }
  .contact__line { font-weight: 300; font-size: 18px; line-height: 1.5; }
  .contact__note { color: var(--green); }
</style>
</head>
<body>
<main class="sheet">

  <section class="card card--front" aria-label="Card front">
    <div class="brand">
      <span class="brand__dot"></span>
      <span class="brand__name"><span class="brand__line">Ridgeline</span><span class="brand__line">Renewal</span></span>
    </div>
    <svg class="card__band" viewBox="0 0 700 60" aria-hidden="true">
      <polygon points="0,32 470,32 470,60 0,60" fill="var(--ink)"/>
      <polygon points="470,32 492,10 700,10 700,14 494,14 474,36 474,60 470,60" fill="var(--ink)"/>
      <polygon points="482,60 482,38 502,20 700,20 700,60" fill="var(--green)"/>
    </svg>
  </section>

  <section class="card card--back" aria-label="Card back">
    <div class="brand">
      <span class="brand__dot"></span>
      <span class="brand__name"><span class="brand__line">Ridgeline</span><span class="brand__line">Renewal</span></span>
    </div>
    <div class="divider"></div>
    <div class="contact">
      <p class="contact__name">Daniel Carver</p>
      <p class="contact__title">Chief Operating Officer</p>
      <p class="contact__line">Ridgeline Renewal LLC</p>
      <p class="contact__line">dcarver@ridgelinerenewal.com</p>
      <p class="contact__line">555-014-2270 <span class="contact__note">(Mobile)</span></p>
    </div>
    <svg class="card__band" viewBox="0 0 700 60" aria-hidden="true">
      <polygon points="0,32 470,32 470,60 0,60" fill="var(--ink)"/>
      <polygon points="470,32 492,10 700,10 700,14 494,14 474,36 474,60 470,60" fill="var(--ink)"/>
      <polygon points="482,60 482,38 502,20 700,20 700,60" fill="var(--green)"/>
    </svg>
  </section>

</main>
</body>
</html>
```